Business card for partnership

Plumbing and hvac company needing a minimal business card. We already have a logo i would like the front of the card just the logo and the back have all info.

Target Market(s)

Commercial facilities

Industry/Entity Type

Plumbing hvac

Contact Information for Business Card

We would like it double sided. Logo big and bold on the front and out info on the back. Our info on back would be name and position phone, email, and location

```html
<!DOCTYPE html>
<html lang="en">
<head>
<meta charset="UTF-8">
<title>Kestrel Mechanical – Business Card</title>
<link href="https://fonts.googleapis.com/css2?family=Montserrat:wght@300;400;500;700&display=swap" rel="stylesheet">
<style>
  :root {
    --charcoal: #333333;
    --orange: #f58a35;
    --paper: #ffffff;
    --ink: #222222;
    --shadow: #dcdcdc;
  }
  * { margin: 0; padding: 0; box-sizing: border-box; }
  html, body {
    width: 1200px;
    height: 1200px;
    overflow: hidden;
    background: var(--paper);
    font-family: "Montserrat", sans-serif;
  }
  .canvas { position: relative; width: 1200px; height: 1200px; }

  .card {
    position: absolute;
    left: 253px;
    width: 701px;
    height: 400px;
    box-shadow: 18px 15px 4px var(--shadow);
  }
  .card-front { top: 121px; background: var(--charcoal); }
  .card-back { top: 658px; background: var(--paper); overflow: hidden; }

  .wordmark {
    position: absolute;
    display: flex;
    align-items: center;
    gap: 12px;
    color: var(--paper);
    font-weight: 700;
    line-height: 1;
  }
  .wordmark-square { background: var(--orange); flex: none; }
  .wordmark-text { display: flex; flex-direction: column; }
  .wordmark-name { letter-spacing: 0.04em; }
  .wordmark-sub { letter-spacing: 0.06em; }

  .card-front .wordmark { left: 50%; top: 50%; transform: translate(-50%, -50%); margin-top: -4px; }
  .card-front .wordmark-square { width: 22px; height: 22px; }
  .card-front .wordmark-name { font-size: 54px; }
  .card-front .wordmark-sub { font-size: 25px; margin-top: 8px; }

  .back-band { position: absolute; left: 0; top: 0; width: 701px; height: 120px; }
  .card-back .wordmark { left: 58px; top: 46px; gap: 8px; }
  .card-back .wordmark-square { width: 12px; height: 12px; }
  .card-back .wordmark-name { font-size: 33px; }
  .card-back .wordmark-sub { font-size: 15px; margin-top: 5px; }

  .holder { position: absolute; left: 68px; top: 290px; }
  .holder-name { font-size: 19px; font-weight: 700; color: var(--ink); line-height: 26px; }
  .holder-title { font-size: 13.5px; font-weight: 300; color: var(--orange); line-height: 20px; }

  .contact-row { position: absolute; left: 403px; display: flex; }
  .contact-icon { width: 24px; height: 24px; flex: none; margin-right: 18px; margin-top: -1px; }
  .contact-text { font-size: 13.5px; font-weight: 400; color: var(--ink); line-height: 21px; letter-spacing: 0.01em; }
  .row-address { top: 147px; }
  .row-phone { top: 231px; }
  .row-web { top: 293px; }
</style>
</head>
<body>
<div class="canvas">

  <section class="card card-front">
    <div class="wordmark">
      <span class="wordmark-square"></span>
      <div class="wordmark-text">
        <span class="wordmark-name">KESTREL</span>
        <span class="wordmark-sub">MECHANICAL</span>
      </div>
    </div>
  </section>

  <section class="card card-back">
    <svg class="back-band" viewBox="0 0 701 120" aria-hidden="true">
      <polygon points="0,0 701,0 701,25 454,25 359,120 0,120" fill="var(--charcoal)"/>
    </svg>
    <div class="wordmark">
      <span class="wordmark-square"></span>
      <div class="wordmark-text">
        <span class="wordmark-name">KESTREL</span>
        <span class="wordmark-sub">MECHANICAL</span>
      </div>
    </div>

    <div class="holder">
      <p class="holder-name">Full Name Here</p>
      <p class="holder-title">Your Title Here</p>
    </div>

    <div class="contact-row row-address">
      <svg class="contact-icon" viewBox="0 0 24 24" aria-hidden="true">
        <path d="M12 22c-4-5.5-7-9-7-12.5a7 7 0 0 1 14 0C19 13 16 16.5 12 22z" fill="none" stroke="var(--orange)" stroke-width="1.4" stroke-linejoin="round"/>
        <circle cx="12" cy="9.5" r="2.6" fill="none" stroke="var(--orange)" stroke-width="1.4"/>
      </svg>
      <p class="contact-text">42 Alder Street 2nd Building<br>Fresno, CA - &nbsp;93721<br>United States</p>
    </div>

    <div class="contact-row row-phone">
      <svg class="contact-icon" viewBox="0 0 24 24" aria-hidden="true">
        <path d="M6.5 3.5l3 4-2 2c1 2.5 3.5 5 6 6l2-2 4 3-2 3c-7 0-14-7-14-14z" fill="none" stroke="var(--orange)" stroke-width="1.3" stroke-linejoin="round"/>
        <path d="M14 6.5a4 4 0 0 1 3.5 3.5M14 3a7.5 7.5 0 0 1 7 7" fill="none" stroke="var(--orange)" stroke-width="1.3" stroke-linecap="round"/>
      </svg>
      <p class="contact-text">+00 (555) 0142 310 (Fax)<br>+00 (555) 0198 640 (Mobile)</p>
    </div>

    <div class="contact-row row-web">
      <svg class="contact-icon" viewBox="0 0 24 24" aria-hidden="true">
        <g fill="none" stroke="var(--orange)" stroke-width="1.2">
          <circle cx="12" cy="12" r="9.5"/>
          <ellipse cx="12" cy="12" rx="4.2" ry="9.5"/>
          <line x1="12" y1="2.5" x2="12" y2="21.5"/>
          <line x1="2.5" y1="12" x2="21.5" y2="12"/>
          <path d="M4 7h16M4 17h16"/>
        </g>
      </svg>
      <p class="contact-text">kestrel@email.com<br>www.YourSite.com</p>
    </div>
  </section>

</div>
</body>
</html>
```